Music video company site re-design :-)

Hi guys,

I run a small music video production company called "Northgate Clip Works".

It's the new year and I'm hoping to update our website design, but am at a bit of a loss - which is where I'm desperately hoping you can help!

I need something cool and contemporary but not utterly terrifying/confusing that your average band manager/solo artist funding their own music video for the first time, won't be put off.

If you can check out our current website (http://www.NorthgateClipWorks.example) I think that would probably help :-)

Target Market(s)

Solo music artists and managers of small groups/bands.

Industry/Entity Type

It Company

Requirements
Must have
• Clear, cool but accessible.

I'll need to be able to embed Pixora videos from our Pixora-plus account into the pages...

http://www.pixora.example/framehousefilms

I'd also like to be able to optimise the site for search engines, so we'll need text and not images with text in them.

I'd also like to include or use images from our videos throughout the site, so if you can include as many of these as possible that would be great.

I've uploaded a zip file with them in, how they are used is up to you guys, but the more the merrier.
Should not have
• Images of cameras, lights, clapper boards etc...

No bloody Times New Roman unless you are really reinventing that wheel or trying to make it look like my nan made my website with clip art.

Also, no god damn emoticons ;-)

```html
<!DOCTYPE html>
<html lang="en">
<head>
<meta charset="utf-8">
<title>Northgate Clip Works – Music Video Production</title>
<link rel="stylesheet" href="https://fonts.googleapis.com/css2?family=Poppins:wght@500;600;700&family=Noto+Sans:wght@400;700&display=swap">
<style>
:root{
  --red:#e8263d;
  --red-dark:#8e0f1e;
  --ink:#000;
  --panel:#1c1c1c;
  --bar:#2b2b2b;
  --text:#f2f2f2;
  --grey:#cfcfcf;
}
*{box-sizing:border-box;margin:0;padding:0}
html,body{width:1200px;height:1188px;overflow:hidden;background:var(--ink)}
body{position:relative;font-family:"Noto Sans",sans-serif;color:var(--text)}
.backdrop{position:absolute;inset:0;
  background:
    radial-gradient(ellipse 220px 520px at 250px 120px,rgba(150,150,150,.35),transparent 70%),
    radial-gradient(ellipse 520px 260px at 560px 980px,rgba(200,200,200,.45),transparent 70%),
    radial-gradient(ellipse 300px 220px at 960px 1000px,rgba(220,220,220,.4),transparent 70%),
    radial-gradient(ellipse 360px 300px at 200px 640px,rgba(170,170,170,.3),transparent 70%),
    linear-gradient(#000 0,#070707 60%,#1a1a1a 85%,#050505 100%)}
.logo{position:absolute;left:72px;top:32px;font-family:"Poppins",sans-serif;font-weight:700;font-size:40px;letter-spacing:-1.5px;color:var(--red)}
.phone{position:absolute;right:62px;top:66px;font-family:"Poppins",sans-serif;font-weight:500;font-size:24px;letter-spacing:1px;color:var(--red)}
.main-nav{position:absolute;left:41px;top:122px;width:1118px;height:56px;border-radius:28px;
  background:linear-gradient(#333,#222);display:flex;align-items:center;justify-content:center;gap:18px;
  font-family:"Poppins",sans-serif;font-weight:600;font-size:25px}
.main-nav a{color:#fff;text-decoration:none}
.main-nav a.current{color:var(--red)}
.main-nav .sep{color:#fff}
.slider{position:absolute;top:202px;width:553px;height:279px;border-radius:18px;overflow:hidden;background:var(--panel)}
.slider.left{left:41px}
.slider.right{left:606px}
.still{position:absolute;inset:0;background:radial-gradient(ellipse at 45% 45%,#8d7a6e,#3b2d2a 55%,#111 100%)}
.play{position:absolute;left:253px;top:114px;width:50px;height:50px;border-radius:50%;border:3px solid #c24a3a;background:rgba(60,60,60,.7)}
.play::after{content:"";position:absolute;left:17px;top:13px;border-left:16px solid #ddd;border-top:10px solid transparent;border-bottom:10px solid transparent}
.reel-title{position:absolute;left:0;right:0;top:100px;text-align:center;font-family:"Poppins",sans-serif;font-weight:700;font-size:44px;color:#ccc;letter-spacing:-1px}
.arrow{position:absolute;top:289px;width:84px;height:84px;border-radius:50%;background:#d9d9d9}
.arrow svg{position:absolute;top:27px;width:30px;height:30px}
.controls{position:absolute;left:0;right:0;bottom:0;height:29px;background:linear-gradient(#6a6a6a,#3d3d3d)}
.col h2{position:absolute;font-family:"Poppins",sans-serif;font-weight:600;font-size:18px;color:var(--red)}
.col p{font-size:14.2px;line-height:20.4px;text-align:justify}
.divider{position:absolute;top:540px;width:3px;height:332px;background:var(--red)}
.pill{position:absolute;width:92px;height:27px;border-radius:14px;background:#fff;color:var(--red);
  font-size:11px;font-weight:700;text-align:center;line-height:27px}
.field{position:absolute;left:869px;width:276px;height:27px;border:1px solid var(--red);background:rgba(0,0,0,.5);
  color:var(--red);font-size:14px;padding-left:7px;line-height:25px}
.btn{position:absolute;top:864px;height:30px;width:134px;background:linear-gradient(#b01b2c,#6a0a15);
  color:#fff;font-size:16px;text-align:center;line-height:30px}
.footer-nav{position:absolute;left:44px;top:1135px;font-size:13px;color:#fff}
.footer-nav .current{color:var(--red)}
.copyright{position:absolute;left:44px;top:1158px;font-size:11px;color:var(--red)}
</style>
</head>
<body>
<div class="backdrop" role="img" aria-label="Black-and-white photo of a band performing on a smoky stage, lit from behind"></div>

<div class="logo">northgateclipworks</div>
<div class="phone">Call 07700 900 461</div>

<nav class="main-nav">
  <a class="current">Home</a><span class="sep">|</span>
  <a>Music Video</a><span class="sep">|</span>
  <a>Promo Future</a><span class="sep">|</span>
  <a>Band Site Design</a><span class="sep">|</span>
  <a>Prices</a><span class="sep">|</span>
  <a>Contact Us</a>
</nav>

<section class="slider left">
  <div class="still" role="img" aria-label="Video still of a performer in an ornate silver headdress"></div>
  <div class="play"></div>
</section>
<section class="slider right">
  <div class="reel-title">Showreel 2010</div>
  <div class="controls"></div>
</section>

<div class="arrow" style="left:-1px"><svg style="left:39px" viewBox="0 0 30 30"><path d="M20 3 8 15l12 12" fill="none" stroke="var(--red)" stroke-width="6"/></svg></div>
<div class="arrow" style="left:552px"><svg style="left:14px" viewBox="0 0 30 30"><path d="M10 3l12 12-12 12" fill="none" stroke="var(--red)" stroke-width="6"/></svg></div>
<div class="arrow" style="left:564px"><svg style="left:39px" viewBox="0 0 30 30"><path d="M20 3 8 15l12 12" fill="none" stroke="var(--red)" stroke-width="6"/></svg></div>
<div class="arrow" style="left:1117px"><svg style="left:14px" viewBox="0 0 30 30"><path d="M10 3l12 12-12 12" fill="none" stroke="var(--red)" stroke-width="6"/></svg></div>

<section class="col welcome">
  <h2 style="left:64px;top:506px">Welcome to NorthgateClipWorks.example</h2>
  <div style="position:absolute;left:67px;top:548px;width:381px">
    <p>“ I have a great working relationship with NCW and remain continually impressed with their professionalism throughout any of my projects. ”</p><br>
    <p>We're a London based music video production company that specialise in affordable band promo and music video production - whether it's for unsigned artists, specialist performers or large record labels - no matter what the genre or style of your music/performance, we can help you promote it!</p><br>
    <p>Our music videos have been broadcast on Pulse TV, Pulse Base, Pulse Europe, The Crate, Channel Loud, The Chart Channel, Streetwave Urban, to name a few.</p>
  </div>
  <div class="pill" style="left:364px;top:871px">Read More</div>
</section>
<div class="divider" style="left:474px"></div>

<section class="col promo">
  <h2 style="left:503px;top:506px">Promo Package</h2>
  <div role="img" aria-label="Video still of a singer in a red top against purple stage lights" style="position:absolute;left:505px;top:551px;width:303px;height:163px;background:linear-gradient(90deg,#1a0a2e,#5b2a9a 30%,#c23040 50%,#5b2a9a 70%,#1a0a2e)"></div>
  <div style="position:absolute;left:505px;top:714px;width:303px;height:26px;background:linear-gradient(#6a6a6a,#3d3d3d)"></div>
  <div style="position:absolute;left:489px;top:752px;width:327px">
    <p>Great music isn't enough. People need to hear it, but sometimes they need to see it. Seeing a performance will help fans connect with a performer or group in ways that the music alone never could.</p>
  </div>
  <div class="pill" style="left:724px;top:871px">Read More</div>
</section>
<div class="divider" style="left:837px"></div>

<section class="col contact">
  <h2 style="left:869px;top:506px">Contact Us</h2>
  <div style="position:absolute;left:868px;top:544px;width:276px">
    <p>Advice or to chat about what you have in mind for your next music video. For more information Please Fill the form or</p>
    <p style="text-align:right">call 07700 900 461</p>
  </div>
  <div class="field" style="top:658px;padding-left:28px">Name:</div>
  <div class="field" style="top:694px">Phone No:</div>
  <div class="field" style="top:730px;padding-left:28px">E-mail:</div>
  <div class="field" style="top:766px;height:84px">Comments:</div>
  <div class="btn" style="left:871px">Clear</div>
  <div class="btn" style="left:1010px">Send</div>
</section>

<footer>
  <div class="footer-nav"><span class="current">Home</span> | Music Video | Promo Future | Band Site Design | Prices | Contact Us | Sitemap</div>
  <div class="copyright">Copyright © 2003-2011 Northgateclipworks. All rights reserved. / Terms of Service / Privacy Plicy</div>
</footer>
</body>
</html>
```